Sunny Trails and joy Business card

I have a logo, but will like a business card design. Is for a travel agency in Mexico. We focus in family experiences.

I will liek some thing different and unique, from the traditional business card, something to get remmeber for.

Business card information:

Leandro R. Quiroga
leandro@sunnytrailsjoy.example

Alameda 742, 3 piso
Col. Tepalcatl
Mexico, D.F. 04910

office: (55) 4821-7390
mobile: (55) 7034-1258

www.sunnytrailsjoy.example
@sunnytjoy
blog: sunnytrailsandjoy.blog.example
facebook: SunnyTrailsAndJoy

```html
<!DOCTYPE html>
<html lang="es">
<head>
<meta charset="utf-8">
<title>Sunny Trails and joy – Business card</title>
<link rel="stylesheet" href="https://fonts.googleapis.com/css2?family=Cabin:wght@400;600;700&display=swap">
<style>
  :root {
    --ink: #1d56d6;
    --ink-dark: #1e4aa8;
    --band-dark: #2f6fe6;
    --band-mid: #8fd3f2;
    --band-light: #bfe8f7;
    --sky: #d8f3f6;
    --paper: #ffffff;
    --frame: #1a1a1a;
  }
  * { margin: 0; padding: 0; box-sizing: border-box; }
  html, body { width: 909px; height: 1200px; overflow: hidden; background: var(--paper); }
  body { position: relative; font-family: "Cabin", sans-serif; color: var(--ink); }

  .card-front, .card-back { position: absolute; left: 0; width: 909px; }
  .card-front { top: 0; height: 530px; }
  .card-back {
    top: 670px; left: 2px; width: 891px; height: 524px;
    border: 2px solid var(--frame);
  }

  .brand { position: absolute; display: flex; align-items: center; justify-content: center; }
  .brand-dot { position: absolute; border-radius: 50%; background: var(--sky); }
  .brand-name {
    position: relative; font-weight: 700; color: var(--ink-dark);
    white-space: nowrap; text-align: center; line-height: 1;
  }
  .card-front .brand { left: 44px; top: 53px; width: 440px; height: 275px; }
  .card-front .brand-dot { width: 230px; height: 230px; left: 105px; top: 22px; }
  .card-front .brand-name { font-size: 42px; }
  .card-back .brand { left: 40px; top: 90px; width: 810px; height: 345px; }
  .card-back .brand-dot { width: 300px; height: 300px; left: 255px; top: 22px; }
  .card-back .brand-name { font-size: 74px; }

  .contact { position: absolute; left: 470px; top: 182px; width: 334px; text-align: center; }
  .contact-name { font-weight: 700; font-size: 27px; color: var(--ink-dark); line-height: 33px; }
  .contact-line { font-size: 23px; line-height: 32px; }

  .address { position: absolute; left: 57px; top: 380px; font-size: 23px; line-height: 32px; }
  .online { position: absolute; left: 476px; top: 370px; font-size: 19.5px; line-height: 27.5px; }

  .bands { position: absolute; display: flex; flex-direction: column; gap: 3px; }
  .bands span { display: block; height: 6px; }
  .bands .b1 { background: var(--band-dark); }
  .bands .b2 { background: var(--band-mid); }
  .bands .b3 { background: var(--band-light); }
  .card-front .bands { left: 12px; top: 499px; width: 894px; }
  .card-back .bands { left: 0; width: 887px; }
  .card-back .bands-top { top: 23px; }
  .card-back .bands-bottom { top: 472px; flex-direction: column-reverse; }
</style>
</head>
<body>
  <section class="card-front">
    <div class="brand">
      <span class="brand-dot"></span>
      <span class="brand-name">Sunny Trails and joy</span>
    </div>

    <div class="contact">
      <p class="contact-name">Leandro R. Quiroga</p>
      <p class="contact-line">leandro@sunnytrailsjoy.example</p>
      <p class="contact-line">office: (55) 4821-7390</p>
      <p class="contact-line">mobile: (55) 7034-1258</p>
    </div>

    <div class="address">
      <p>Alameda 742, 3 piso</p>
      <p>Col. Tepalcatl</p>
      <p>Mexico, D.F. 04910</p>
    </div>

    <div class="online">
      <p>www.sunnytrailsjoy.example</p>
      <p>@sunnytjoy</p>
      <p>blog: sunnytrailsandjoy.blog.example</p>
      <p>facebook: SunnyTrailsAndJoy</p>
    </div>

    <div class="bands"><span class="b1"></span><span class="b2"></span><span class="b3"></span></div>
  </section>

  <section class="card-back">
    <div class="bands bands-top"><span class="b1"></span><span class="b2"></span><span class="b3"></span></div>
    <div class="brand">
      <span class="brand-dot"></span>
      <span class="brand-name">Sunny Trails and joy</span>
    </div>
    <div class="bands bands-bottom"><span class="b1"></span><span class="b2"></span><span class="b3"></span></div>
  </section>
</body>
</html>
```